Modify mobile web Photoshop design to make them look great

We need to choose and refine the stock image to look great on 5 mobile web pages: 1) Hourglass image on home screen, 2) Sofa image on registration screen, 3) Loveseat image on login screen, 4) Lamp for reminder screen, and 5) Bed for ratings / score screen. Sample photos denote what customer wants, but they are just downloaded from Brindo, and is not purchased stock photos. Designers need to show that the updated photos used are properly purchased from stock photo source. Photoshop files for all 5 mobile web pages are provided. Artists are requested to edit and submit the 5 photoshop files and make them look as good as possible with the constraints above. No change is needed on the layout or anything beside the 5 stock images, but subtle refinements are OK if you believe it would improve the overall design without affecting the art direction.

Target Market(s)

Travel, Lifestyle

Industry/Entity Type

Hospitality

Font styles to use
Sans Serif

Requirements
Must have
• Stock photos must be properly licensed, artists must put updated stock photos back into supplied photoshop source files, updated look and feel should have the same general art direction, images must be hourglass, sofa, loveseat, lamp and bed
Nice to have
• Minor and very subtle touchup of other elements without affecting any design work of the layout such as color scheme
Should not have
• Should not affect art direction, identity and color of all design and layout elements, should not use stock image other than the types specified (hourglass, sofa, loveseat, lamp and bed), should not use images not licensed from stock photo sites

```html
<!DOCTYPE html>
<html lang="en">
<head>
<meta charset="utf-8">
<title>nestlo.co – Rate Your Stay</title>
<link href="https://fonts.googleapis.com/css2?family=Montserrat:wght@300;400;500;600;700;800&display=swap" rel="stylesheet">
<style>
  :root{
    --ink:#111111;
    --white:#ffffff;
    --plum:#9e0f72;
    --plum-button:#a80f7a;
    --plum-dark:#6e0a4f;
    --lilac:#b98bd8;
    --star-off:#cfcfcf;
    --star-off-edge:#a9a9a9;
    --line:#8a8a8a;
    --box-edge:#d7d7d7;
    --placeholder:#bdbdbd;
    --card:rgba(255,255,255,0.82);
  }
  *{box-sizing:border-box;margin:0;padding:0}
  html,body{width:675px;height:1200px;overflow:hidden;background:var(--white)}
  body{font-family:"Montserrat",Arial,sans-serif;color:var(--ink);position:relative}

  .status-bar{position:absolute;top:0;left:0;width:675px;height:36px;display:flex;align-items:center;justify-content:space-between;padding:0 12px 0 24px;font-size:17px;font-weight:500}
  .status-bar .carrier{display:flex;align-items:center;gap:6px}
  .status-bar .clock{position:absolute;left:0;right:0;text-align:center;font-weight:600}
  .battery{width:40px;height:16px;border:1.5px solid var(--ink);border-radius:4px;padding:2px;position:relative}
  .battery::before{content:"";display:block;width:100%;height:100%;background:var(--ink);border-radius:1.5px}
  .battery::after{content:"";position:absolute;right:-5px;top:4px;width:3px;height:6px;background:var(--ink);border-radius:0 2px 2px 0}

  .app-header{position:absolute;top:36px;left:0;width:675px;height:90px;background:var(--white);display:flex;align-items:center;justify-content:center}
  .app-header .back{position:absolute;left:34px;top:29px}
  .app-header .menu{position:absolute;right:36px;top:30px}
  .brand-name{font-size:44px;font-weight:800;letter-spacing:-2px;color:var(--ink)}

  .room-backdrop{position:absolute;top:126px;left:0;width:675px;height:1074px;
    background:linear-gradient(180deg,#f1d3d6 0%,#eadfe3 22%,#e4e2e8 50%,#dcdce3 78%,#cfcdd6 100%)}

  .review-card{position:absolute;left:27px;top:238px;width:616px;height:803px;background:var(--card);border-radius:8px;box-shadow:0 2px 8px rgba(0,0,0,0.12)}

  .reviewer{position:absolute;left:13px;top:13px;display:flex;align-items:center;gap:13px}
  .avatar{width:62px;height:62px;border-radius:50%;background:var(--white);border:1px solid #c9c9c9;display:flex;align-items:center;justify-content:center}
  .reviewer-name{font-size:23px;font-weight:600;letter-spacing:0.3px}
  .divider{position:absolute;left:10px;top:85px;width:596px;height:1px;background:var(--line)}

  .hotel-photo{position:absolute;left:10px;top:97px;width:596px;height:219px;
    background:linear-gradient(90deg,#b8ab94 0%,#d8d0c2 25%,#9d8a74 48%,#c9bba6 70%,#8e7d68 100%)}
  .hotel-caption{position:absolute;left:10px;top:262px;width:596px;height:54px;background:rgba(20,20,20,0.82);color:var(--white);font-size:22px;font-weight:500;letter-spacing:0.4px;padding:13px 0 0 21px}

  .section-title{position:absolute;left:10px;top:346px;height:54px;display:flex;align-items:center;border-left:7px solid var(--lilac);padding-left:16px;font-size:21px;font-weight:600;letter-spacing:0.6px;text-transform:uppercase}

  .rating-box{position:absolute;left:30px;top:412px;width:558px;height:102px;background:var(--white);border:1px solid var(--box-edge);border-radius:4px;display:flex;align-items:center;justify-content:space-between;padding:0 26px 0 26px}
  .stars{display:flex;gap:17px}
  .rating-value{font-size:51px;font-weight:700;color:var(--plum);letter-spacing:1px}

  .comment-box{position:absolute;left:30px;top:536px;width:558px;height:165px;background:var(--white);border:1px solid var(--box-edge);border-radius:4px;padding:22px 24px;font-size:16px;font-weight:300;line-height:22px;color:var(--placeholder)}

  .submit-button{position:absolute;left:31px;top:718px;width:558px;height:62px;background:var(--plum-button);border-radius:3px;color:var(--white);font-size:20px;font-weight:700;letter-spacing:0.4px;display:flex;align-items:center;justify-content:center}
</style>
</head>
<body>
  <div class="status-bar">
    <div class="carrier">Carrier
      <svg width="18" height="13" viewBox="0 0 18 13"><path d="M9 12.5l2.6-3a3.6 3.6 0 0 0-5.2 0z" fill="#111"/><path d="M2.2 5.6a9.6 9.6 0 0 1 13.6 0M4.6 8.2a6.2 6.2 0 0 1 8.8 0" stroke="#111" stroke-width="2" fill="none" stroke-linecap="round"/></svg>
    </div>
    <div class="clock">1:23 PM</div>
    <div class="battery"></div>
  </div>

  <header class="app-header">
    <svg class="back" width="22" height="34" viewBox="0 0 22 34"><path d="M18 3L5 17l13 14" stroke="#111" stroke-width="4" fill="none" stroke-linecap="round" stroke-linejoin="round"/></svg>
    <div class="brand-name">nestlo.co</div>
    <svg class="menu" width="36" height="32" viewBox="0 0 36 32"><g stroke="#111" stroke-width="4.5" stroke-linecap="round"><path d="M2 3h32M2 16h32M2 29h32"/></g></svg>
  </header>

  <div class="room-backdrop" role="img" aria-label="Softly faded photo of a bright hotel bedroom with chandelier and tufted headboard"></div>

  <main class="review-card">
    <div class="reviewer">
      <div class="avatar">
        <svg width="32" height="40" viewBox="0 0 32 40"><circle cx="16" cy="11" r="8.5" fill="none" stroke="#111" stroke-width="2"/><path d="M2 38c0-8 5-14 14-14s14 6 14 14z" fill="none" stroke="#111" stroke-width="2" stroke-linejoin="round"/></svg>
      </div>
      <div class="reviewer-name">Marcus Lee</div>
    </div>
    <div class="divider"></div>

    <div class="hotel-photo" role="img" aria-label="Photo of a luxury hotel bedroom with a large bed, padded headboard and bedside lamp"></div>
    <div class="hotel-caption">Hotel Serrano Harbour</div>

    <h2 class="section-title">Please rate overall services</h2>

    <div class="rating-box">
      <div class="stars">
        <svg width="46" height="44" viewBox="0 0 46 44"><path d="M23 2l6.2 13.4 14.6 1.7-10.8 10 2.9 14.4L23 34.3 10.1 41.5 13 27.1 2.2 17.1l14.6-1.7z" fill="var(--plum)" stroke="var(--plum-dark)" stroke-width="1.5" stroke-linejoin="round"/></svg>
        <svg width="46" height="44" viewBox="0 0 46 44"><path d="M23 2l6.2 13.4 14.6 1.7-10.8 10 2.9 14.4L23 34.3 10.1 41.5 13 27.1 2.2 17.1l14.6-1.7z" fill="var(--plum)" stroke="var(--plum-dark)" stroke-width="1.5" stroke-linejoin="round"/></svg>
        <svg width="46" height="44" viewBox="0 0 46 44"><path d="M23 2l6.2 13.4 14.6 1.7-10.8 10 2.9 14.4L23 34.3 10.1 41.5 13 27.1 2.2 17.1l14.6-1.7z" fill="var(--plum)" stroke="var(--plum-dark)" stroke-width="1.5" stroke-linejoin="round"/></svg>
        <svg width="46" height="44" viewBox="0 0 46 44"><path d="M23 2l6.2 13.4 14.6 1.7-10.8 10 2.9 14.4L23 34.3 10.1 41.5 13 27.1 2.2 17.1l14.6-1.7z" fill="var(--plum)" stroke="var(--plum-dark)" stroke-width="1.5" stroke-linejoin="round"/></svg>
        <svg width="46" height="44" viewBox="0 0 46 44"><path d="M23 2l6.2 13.4 14.6 1.7-10.8 10 2.9 14.4L23 34.3 10.1 41.5 13 27.1 2.2 17.1l14.6-1.7z" fill="var(--star-off)" stroke="var(--star-off-edge)" stroke-width="1.5" stroke-linejoin="round"/></svg>
      </div>
      <div class="rating-value">4.0</div>
    </div>

    <div class="comment-box">Tell others what you think about us. Would you recommend it, and&nbsp; why?</div>

    <div class="submit-button">SUBMIT FEEDBACK</div>
  </main>
</body>
</html>
```